Prepared Meal Company Needs Menu Design

We are a pre-prepared meal delivery company called Greel Brantwick.

We have a menu in excel but needs to be designed to look good and appealing to customers. The menu should be clean, easy to ready, and show:Title (Pupusa)Tags (V, V+, GF - Use a cool vegan logo for the V+ and logo for vegetarian V symbol)Price (12.99)DescriptionBrand colors are orange white and green. Design is clean, crisp and can incorporate natural elements like leaf shaped symbols, etc. Screenshots from our website attached for inspiration.

Target Market(s)

Broad demographics

Industry/Entity Type

Restaurant

Font styles to use
Sans Serif

Requirements
Must have
• The menu design should be commensurate with the website under development
• https://greelbrantwick.tavlorix.com
Nice to have
• Should have appropriate graphics
Should not have
• Modifiers do not need to be shown (these are shown in the excel only).

```html
<!DOCTYPE html>
<html lang="en">
<head>
<meta charset="utf-8">
<title>Greel Brantwick Menu</title>
<link rel="stylesheet" href="https://fonts.googleapis.com/css2?family=Saira+Semi+Condensed:wght@400;600;700&family=Saira:ital,wght@1,400&display=swap">
<style>
:root{
  --bg:#ffffff;
  --paper:#f6f3ea;
  --green:#0a7f3b;
  --orange:#f07a1a;
  --ink:#2e2e2e;
  --grey:#555555;
}
*{margin:0;padding:0;box-sizing:border-box}
html,body{width:1200px;height:2604px;overflow:hidden;background:var(--bg)}
body{position:relative;font-family:"Saira Semi Condensed",Arial,sans-serif;color:var(--ink)}
.page{position:absolute;left:92px;width:1016px;height:1226px;background:var(--paper);box-shadow:0 4px 14px rgba(0,0,0,.22)}
.page-one{top:70px}
.page-two{top:1344px}
.page-band{position:absolute;left:0;right:0;bottom:0;height:22px;background:var(--green)}
.brand{position:absolute;top:34px;left:0;right:0;display:flex;justify-content:center;align-items:center;gap:10px}
.brand-dot{width:22px;height:22px;border-radius:50%;background:var(--orange)}
.brand-name{font-weight:700;font-size:24px;color:var(--orange);letter-spacing:1px}
.section{position:absolute;left:194px;width:637px;height:34px;display:flex;align-items:center;justify-content:center}
.section::before{content:"";position:absolute;left:0;right:0;top:50%;height:2px;background:var(--green)}
.section-label{position:relative;background:var(--green);color:#fff;font-weight:700;font-size:21px;padding:0 20px;height:34px;line-height:34px;letter-spacing:.5px}
.item{position:absolute;left:0;right:0;height:90px}
.item-name{position:absolute;left:98px;top:0;width:350px;font-weight:700;font-size:19px;line-height:22px;color:var(--ink)}
.item-desc{position:absolute;left:461px;top:-2px;width:340px;font-family:"Saira",Arial,sans-serif;font-style:italic;font-size:13px;line-height:16px;color:var(--ink)}
.item-price{position:absolute;right:106px;top:0;font-weight:700;font-size:22px;color:var(--grey)}
.tags{position:absolute;left:125px;top:32px;display:flex;align-items:center;gap:14px;height:44px}
.tags.second{top:86px}
.tags.plain{left:181px;top:26px}
.tag-text{font-weight:600;font-size:16px;color:var(--ink)}
.badge{width:42px;height:42px;display:block}
.sep{position:absolute;left:129px;width:766px;border-top:2px dashed var(--orange);opacity:.8}
</style>
</head>
<body>
<svg width="0" height="0" style="position:absolute" aria-hidden="true">
  <defs>
    <symbol id="badge-veg" viewBox="0 0 42 42">
      <circle cx="21" cy="21" r="20" fill="#0a7f3b"/>
      <circle cx="21" cy="21" r="15" fill="none" stroke="#fff" stroke-width="1.5"/>
      <text x="21" y="27" text-anchor="middle" font-family="Arial,sans-serif" font-weight="700" font-size="17" fill="#fff">V</text>
    </symbol>
    <symbol id="badge-vegan" viewBox="0 0 42 42">
      <circle cx="21" cy="21" r="20" fill="#0a7f3b"/>
      <circle cx="21" cy="21" r="15" fill="none" stroke="#fff" stroke-width="1.5"/>
      <text x="21" y="24.5" text-anchor="middle" font-family="Arial,sans-serif" font-weight="700" font-size="9" fill="#fff">VEGAN</text>
    </symbol>
  </defs>
</svg>

<section class="page page-one">
  <div class="brand"><span class="brand-dot"></span><span class="brand-name">Greel Brantwick</span></div>

  <div class="section" style="top:155px"><span class="section-label">BREAKFAST - All Menu Items Soy Free</span></div>

  <div class="item" style="top:207px">
    <div class="item-name">Cinnamon-Apple Sunrise Oats</div>
    <div class="item-desc">Almond Milk &amp; Ceylon Cinnamon, Marinated Golden Raisins, Macca Powder, Apple-Pecan Crumble</div>
    <div class="item-price">6.99</div>
    <div class="tags"><svg class="badge"><use href="#badge-vegan"/></svg><span class="tag-text">GF</span></div>
  </div>
  <div class="sep" style="top:285px"></div>

  <div class="item" style="top:299px">
    <div class="item-name">Acai Yogurt</div>
    <div class="item-desc">Coconut, Goji, Seasonal Fruit, Crunchy Chia Seeds, Ceylon Cinnamon</div>
    <div class="item-price">7.99</div>
    <div class="tags"><svg class="badge"><use href="#badge-veg"/></svg><span class="tag-text">GF</span></div>
  </div>
  <div class="sep" style="top:376px"></div>

  <div class="item" style="top:390px">
    <div class="item-name">Harvest 7:3 Cereal &amp; Yogurt</div>
    <div class="item-desc">Apricot-Pear Compote, Almond &amp; Saba Drizzle</div>
    <div class="item-price">7.49</div>
    <div class="tags"><svg class="badge"><use href="#badge-veg"/></svg></div>
  </div>
  <div class="sep" style="top:468px"></div>

  <div class="item" style="top:482px">
    <div class="item-name">St. Benedict's Eggs</div>
    <div class="item-desc">2 Soft Yolk Eggs over Rosemary Polenta, Caramelized Onion, Mushrooms &amp; Asparagus, Lemon</div>
    <div class="item-price">9.49</div>
    <div class="tags"><svg class="badge"><use href="#badge-veg"/></svg><span class="tag-text">Dairy Free</span></div>
  </div>
  <div class="sep" style="top:567px"></div>

  <div class="item" style="top:581px">
    <div class="item-name">Pomegranate &amp; Saffron Shakshuka</div>
    <div class="item-desc">2 Soft Yolk Eggs over Roasted Tomatoes, Onions &amp; Peppers, Garden Herb Oil, Rosemary, Oregano &amp; Thyme with Handmade Gluten-Free Flatbread</div>
    <div class="item-price">10.99</div>
    <div class="tags"><svg class="badge"><use href="#badge-veg"/></svg><span class="tag-text">GF Dairy Free</span></div>
  </div>
  <div class="sep" style="top:663px"></div>

  <div class="item" style="top:677px">
    <div class="item-name">Sweet Potato Hash</div>
    <div class="item-desc">Broccolini, Cherry Tomato, Asparagus, Roasted Peppers &amp; Onions, Rosemary-Nutritional Yeast</div>
    <div class="item-price">8.99</div>
    <div class="tags"><svg class="badge"><use href="#badge-vegan"/></svg><span class="tag-text">GF</span></div>
  </div>
  <div class="sep" style="top:763px"></div>

  <div class="item" style="top:777px">
    <div class="item-name">Mom's Frittata</div>
    <div class="item-desc">Roasted Cherry Tomato, Goat Cheese &amp; Baby Spinach with Sweet Potato Homefries</div>
    <div class="item-price">11.99</div>
    <div class="tags"><svg class="badge"><use href="#badge-veg"/></svg><span class="tag-text">GF</span></div>
  </div>
  <div class="sep" style="top:861px"></div>

  <div class="item" style="top:875px">
    <div class="item-name">Country Style Breakfast Sandwich</div>
    <div class="item-desc">Arugula, Goat Cheese, Cherry Tomatoes &amp; Lemon with Mom's Frittata on Harvest 7:3 Bread</div>
    <div class="item-price">13.99</div>
    <div class="tags"><svg class="badge"><use href="#badge-veg"/></svg></div>
  </div>

  <div class="section" style="top:958px"><span class="section-label">APPETIZERS</span></div>

  <div class="item" style="top:1015px">
    <div class="item-name">Avocado Super-Toast</div>
    <div class="item-desc">Shaved Fennel &amp; Golden Beets, Avocado, Garden Herb Oil, Lemon Juice, Ground Flax, Hemp Seed, Golden Raisin &amp; Moringa on Harvest 7:3 Sprouted Whole</div>
    <div class="item-price">9.49</div>
    <div class="tags"><svg class="badge"><use href="#badge-vegan"/></svg><span class="tag-text">GF with Flatbread</span></div>
  </div>
  <div class="sep" style="top:1106px"></div>

  <div class="item" style="top:1120px">
    <div class="item-name">Pupusa</div>
    <div class="item-desc">Coconut, Goji, Seasonal Fruit, Crunchy Chia Seeds, Ceylon Cinnamon</div>
    <div class="item-price">9.49</div>
    <div class="tags"><svg class="badge"><use href="#badge-veg"/></svg><span class="tag-text">GF</span></div>
  </div>

  <div class="page-band"></div>
</section>

<section class="page page-two">
  <div class="brand"><span class="brand-dot"></span><span class="brand-name">Greel Brantwick</span></div>

  <div class="item" style="top:161px">
    <div class="item-name">Pupusa Deluxe</div>
    <div class="item-desc">Sous Vide Bison Shortrib, Goat Cheese, Ayocote &amp; Avocado Puree, Nopales, Cilantro-Lime Yogurt, Inca Corn Crumble, Tropical Acai Hot Sauce</div>
    <div class="item-price">13.99</div>
    <div class="tags plain"><span class="tag-text">GF</span></div>
  </div>
  <div class="sep" style="top:222px"></div>

  <div class="item" style="top:236px">
    <div class="item-name">Egyptian Flatbread</div>
    <div class="item-desc">Honey-Chamomile Yogurt, Braised Cherry Tomatoes, Sumac &amp; Pistachio Dukkha, Garlic &amp; Micro Radish on Handmade Gluten-Free Flatbread</div>
    <div class="item-price">11.99</div>
    <div class="tags"><svg class="badge"><use href="#badge-veg"/></svg><span class="tag-text">GF</span></div>
  </div>
  <div class="sep" style="top:326px"></div>

  <div class="item" style="top:340px">
    <div class="item-name">Green Street Tacos</div>
    <div class="item-desc">Sugar Snap Peas, Guacamole, Radish &amp; Inca Corn Crumble on 2 Handmade Corn Tortillas.</div>
    <div class="item-price">9.99</div>
    <div class="tags"><svg class="badge"><use href="#badge-vegan"/></svg><span class="tag-text">GF</span></div>
  </div>
  <div class="sep" style="top:427px"></div>

  <div class="item" style="top:441px">
    <div class="item-name">Marinated Squash Tacos</div>
    <div class="item-desc">Chayote Escabeche, Jalapeno, Guacamole, Carrots, Radish, Pepitas &amp; Cilantro, on 2 Handmade Corn Tortillas.</div>
    <div class="item-price">9.99</div>
    <div class="tags"><svg class="badge"><use href="#badge-veg"/></svg><span class="tag-text">GF</span></div>
  </div>
  <div class="sep" style="top:518px"></div>

  <div class="item" style="top:532px">
    <div class="item-name">Soft Yolk Egg &amp;<br>Avocado "Toast" Flatbread</div>
    <div class="item-desc">Ayocote &amp; Avocado Puree, Guacamole, Sunflower Seeds, Inca Corn, Arugula, Lime &amp; Soft Yolk Egg on Handmade Gluten-Free Flatbread</div>
    <div class="item-price">10.99</div>
    <div class="tags" style="top:52px"><svg class="badge"><use href="#badge-veg"/></svg><span class="tag-text">GF</span></div>
  </div>

  <div class="section" style="top:642px"><span class="section-label">SOUPS</span></div>

  <div class="item" style="top:694px">
    <div class="item-name">Seasonal Vegetable Minestrone<br>with Free Range Turkey Meatballs</div>
    <div class="item-desc">Ayocote Beans, Roasted Tomatoes, Carrots, Onions &amp; Bell Pepper, Snap Peas, Garnett Yam, Rosemary &amp; Oregano</div>
    <div class="item-price">9.49</div>
    <div class="tags plain" style="top:44px"><span class="tag-text">GF</span></div>
  </div>
  <div class="sep" style="top:772px"></div>

  <div class="item" style="top:786px">
    <div class="item-name">Sweet Carrot &amp; Coriander Soup</div>
    <div class="item-desc">Garden Herb Oil, Cilantro, Toasted Pepita</div>
    <div class="item-price">5.99</div>
    <div class="tags"><svg class="badge"><use href="#badge-vegan"/></svg><span class="tag-text">GF</span></div>
  </div>
  <div class="sep" style="top:878px"></div>

  <div class="item" style="top:892px">
    <div class="item-name">Butternut Squash &amp; Nopale Chili</div>
    <div class="item-desc">Arugula, Goat Cheese, Cherry Tomatoes &amp; Lemon with Mom's Frittata on Harvest 7:3 Bread</div>
    <div class="item-price">13.99</div>
    <div class="tags"><svg class="badge"><use href="#badge-veg"/></svg><span class="tag-text">GF Dairy Free</span></div>
    <div class="tags second"><svg class="badge"><use href="#badge-vegan"/></svg><span class="tag-text">if No Goat Cheese</span></div>
  </div>
  <div class="sep" style="top:1035px"></div>

  <div class="item" style="top:1049px">
    <div class="item-name">Ansel's Chicken Soup</div>
    <div class="item-desc">Gluten-Free Sorghum Penne, Root Vegetables, Oregano &amp; Peppercorns on the Vine</div>
    <div class="tags plain"><span class="tag-text">GF with Flatbread</span></div>
  </div>

  <div class="page-band"></div>
</section>
</body>
</html>
```